Investment website design - investing in mutual funds

I need a design of a website (only homepage for now) dedicated to investment in mutual funds. Attached is a mock up with all the elements the homepage design should contain. The homepage should contain a logo in the upper left corner, the domain the website will run on is www.morvatelsko.cz , in the upper right corner there should be 2 buttons or links SIGN UP / SIGN IN. The bottom of the homepage should contain links to ABOUT US, FAQ, PRIVACY POLICY, CONTACT US.
Now the main elements on the homepage
1) Video that will explain how the investment works exactly, under this video we will have 3 illustrated icons like the ones attached (see 2nd attachement) that will show the potential investor what exactly they could get when investing with us (education for kids, happy life after they retire, regular monthly payment for the rest of their life).
2) On the right side next to the video we will have a calculator where a potential investor can play with the numbers, the investor can fill in the MONTHLY PAYMENT that he wants to invest regularly every month, the time frame of the investment - for how long he wants to invest. Once the potential investor selects those 2 variables we will calculate for him 2 options - either he can get a ONE TIME PAYOUT once he reaches his investment horizon or he can get a regular monthly payment for the rest of his life. Under the laculator there will be a button 'I want to invest ->'. The functionality of the calculator should be similar to the calculator that can be found here http://www.brovikbanka.cz/brovik-podilove-fondy/ and https://pelvaro.cz/.
The design should look similar to https://pelvaro.cz/ (font, colors, logo). We prefer white background in the area where we have the video and calculator. We also like the design of www.truvanex.com. Let me know if you have any questions.

```html
<!DOCTYPE html>
<html lang="en">
<head>
<meta charset="utf-8">
<title>morvatelsko – investing in mutual funds</title>
<link href="https://fonts.googleapis.com/css2?family=Roboto+Slab:wght@300;400;700&display=swap" rel="stylesheet">
<style>
  :root{
    --accent:#e8553a;
    --teal:#43b1bf;
    --ink:#2b2b2b;
    --muted:#777;
    --rule:#c9c9c9;
    --track:#dcdcdc;
    --shadow:#d6d6d6;
    --white:#fff;
  }
  *{margin:0;padding:0;box-sizing:border-box}
  html,body{width:1200px;height:618px;overflow:hidden;background:var(--white)}
  body{position:relative;font-family:"Roboto Slab",serif;color:var(--ink)}
  .abs{position:absolute}

  .brand{left:58px;top:25px;font-size:19px;font-weight:700;color:var(--ink);letter-spacing:.2px}
  .auth-btn{top:17px;width:60px;height:22px;background:var(--accent);color:var(--white);
    font-size:9px;font-weight:700;display:flex;align-items:center;justify-content:center;
    box-shadow:3px 3px 0 var(--shadow);text-decoration:none}
  .auth-btn.sign-in{left:1002px}
  .auth-btn.sign-up{left:1071px}

  .video-visual{left:51px;top:86px;width:561px;height:426px;border-radius:12px;
    background:linear-gradient(180deg,#1a1a1a 0%,#1a1a1a 78%,#b9bcbf 86%,#dfe1e3 100%)}
  .video-visual .screen{position:absolute;left:23px;top:22px;width:515px;height:290px;
    background:linear-gradient(180deg,#dff3ee 0%,#dff3ee 62%,#e6cf9e 72%,#f6e6c4 100%)}
  .play{position:absolute;left:246px;top:137px;width:66px;height:66px;border-radius:50%;
    background:var(--teal);border:5px solid var(--white)}
  .play::after{content:"";position:absolute;left:22px;top:15px;border-left:20px solid var(--white);
    border-top:13px solid transparent;border-bottom:13px solid transparent}

  .calc{left:682px;width:454px}
  .calc-title{left:680px;top:80px;font-size:30px;font-weight:700;letter-spacing:.3px;white-space:nowrap}
  .row{position:absolute;left:0;width:454px;display:flex;justify-content:space-between;align-items:flex-end;
    border-bottom:1px dashed var(--rule);padding:0 1px 3px 1px}
  .row .label{font-size:11px;font-weight:300;color:var(--muted)}
  .row .value{font-size:14px;font-weight:700;color:var(--ink)}
  .length-label{left:683px;top:158px;font-size:11px;font-weight:700;color:#555}
  .slider{left:685px;top:190px;width:451px;height:40px}
  .slider .tip{position:absolute;left:48px;top:-5px;font-size:8px;font-weight:700;color:var(--accent)}
  .slider .track{position:absolute;left:0;top:14px;width:451px;height:2px;background:var(--track)}
  .slider .fill{position:absolute;left:0;top:14px;width:62px;height:2px;background:var(--teal)}
  .slider .knob{position:absolute;left:54px;top:7px;width:16px;height:16px;border-radius:50%;
    background:var(--white);border:4px solid var(--accent)}
  .slider .min,.slider .max{position:absolute;top:29px;font-size:10px;font-weight:700;color:var(--muted)}
  .slider .min{left:0}
  .slider .max{right:2px}
  .or{left:682px;top:276px;font-size:10px;font-weight:300;color:var(--muted)}
  .invest-btn{left:942px;top:367px;width:187px;height:40px;background:var(--accent);color:var(--white);
    font-size:15px;font-weight:700;display:flex;align-items:center;justify-content:center;
    box-shadow:6px 6px 0 var(--shadow);letter-spacing:.3px;text-decoration:none}

  .footer{left:0;top:471px;width:1200px;height:147px;background:var(--teal);color:var(--white)}
  .footer-nav{position:absolute;left:178px;top:74px;display:flex;gap:23px;font-size:14px;font-weight:700}
  .footer-nav a{color:var(--white);text-decoration:none}
  .copyright{position:absolute;left:247px;top:112px;font-size:9.5px;font-weight:300}
  .benefit{position:absolute;top:31px;width:120px;text-align:center}
  .benefit .badge{width:72px;height:72px;border-radius:50%;background:var(--white);margin:0 auto;
    display:flex;align-items:center;justify-content:center}
  .benefit .caption{margin-top:16px;font-size:11px;font-weight:700}
  .benefit.kids{left:732px}
  .benefit.income{left:874px}
  .benefit.retirement{left:1026px}
</style>
</head>
<body>
  <div class="abs brand">morvatelsko</div>
  <a class="abs auth-btn sign-in" href="#">SIGN IN</a>
  <a class="abs auth-btn sign-up" href="#">SIGN UP</a>

  <div class="abs video-visual" role="img" aria-label="Desktop monitor showing an explainer video illustration: stacks of coins growing along a rising chart, hands holding a clipboard with checklist, play button in the centre">
    <div class="screen"><div class="play"></div></div>
  </div>

  <h1 class="abs calc-title">OUR ONLINE CALCULATOR</h1>

  <div class="abs calc" style="top:0">
    <div class="row" style="top:122px"><span class="label">Regular monthly investment:</span><span class="value">4,99 % p.a.</span></div>
  </div>
  <div class="abs length-label">Length of investment</div>
  <div class="abs slider">
    <span class="tip">6 years</span>
    <div class="track"></div><div class="fill"></div><div class="knob"></div>
    <span class="min">0</span><span class="max">30 years</span>
  </div>
  <div class="abs calc" style="top:0">
    <div class="row" style="top:249px"><span class="label">One timepayment:</span><span class="value">44 měsíců</span></div>
    <div class="row" style="top:296px"><span class="label">Monthly payment:</span><span class="value">11 763 Kč</span></div>
  </div>
  <div class="abs or">OR</div>
  <a class="abs invest-btn" href="#">I WANT TO INVEST</a>

  <footer class="abs footer">
    <nav class="footer-nav">
      <a href="#">About us</a><a href="#">FAQ</a><a href="#">Privacy Policy</a><a href="#">Contact</a>
    </nav>
    <p class="copyright">© 2017 morvatelsko. All rights reserved.</p>

    <div class="benefit kids">
      <div class="badge">
        <svg width="34" height="34" viewBox="0 0 34 34" fill="none" stroke="#43b1bf" stroke-width="2.5">
          <circle cx="17" cy="11" r="6" fill="#43b1bf" stroke="none"/>
          <path d="M17 4 l2 -3"/>
          <rect x="5" y="20" width="24" height="5" rx="2"/>
          <rect x="5" y="27" width="24" height="5" rx="2"/>
        </svg>
      </div>
      <div class="caption">Education for kids</div>
    </div>
    <div class="benefit income">
      <div class="badge">
        <svg width="36" height="32" viewBox="0 0 36 32" fill="#43b1bf">
          <rect x="3" y="21" width="6" height="10" rx="1"/>
          <rect x="11" y="17" width="6" height="14" rx="1"/>
          <rect x="19" y="19" width="6" height="12" rx="1"/>
          <rect x="27" y="12" width="6" height="19" rx="1"/>
          <path d="M3 15 L12 7 L20 12 L31 3" fill="none" stroke="#43b1bf" stroke-width="2.5"/>
          <path d="M26 2 L33 1 L32 8 Z"/>
        </svg>
      </div>
      <div class="caption">Passive income</div>
    </div>
    <div class="benefit retirement">
      <div class="badge">
        <svg width="36" height="32" viewBox="0 0 36 32" fill="#43b1bf">
          <circle cx="25" cy="16" r="7"/>
          <path d="M3 26 Q18 14 33 26 Q18 32 3 26 Z"/>
          <rect x="11" y="10" width="2.5" height="12"/>
          <path d="M4 10 Q12 2 20 10 Q12 6 4 10 Z"/>
        </svg>
      </div>
      <div class="caption">Happy retirment</div>
    </div>
  </footer>
</body>
</html>
```